MS word document templates for consultancy

I need the following templates for my business using my logo as branding.

- General report template
- Letter head template
- Tender proposal template

The templates should be sleek and with minimal colors, but with a small amount of green and grey where appropriate (as per attached logo and email signature). Font should be consistent with the text in the email signature.

```html
<!DOCTYPE html>
<html lang="en">
<head>
<meta charset="utf-8">
<title>Kinward Advisory – Letterhead and Report Templates</title>
<link rel="stylesheet" href="https://fonts.googleapis.com/css2?family=Arimo:wght@400&family=Lexend:wght@400&family=Roboto:wght@400;500;700&family=Roboto+Condensed:wght@400;600&display=swap">
<style>
  :root {
    --green: #2a9a47;
    --ink: #111111;
    --body: #555555;
    --rule: #a8a8a8;
    --backdrop: #9d9d9d;
    --paper: #ffffff;
    --sig: #d9d9d9;
  }
  * { box-sizing: border-box; margin: 0; padding: 0; }
  html, body { width: 1200px; height: 982px; overflow: hidden; background: var(--backdrop); }
  .canvas { position: relative; width: 1200px; height: 982px; }

  .page {
    position: absolute; top: 130px; width: 511px; height: 722px;
    background: var(--paper); overflow: hidden;
  }
  .page--letter { left: 72px; }
  .page--report { left: 617px; }

  .brand {
    position: absolute; top: 38px; left: 0; width: 100%;
    display: flex; justify-content: center; align-items: center; gap: 7px;
    font-family: "Lexend", sans-serif; font-weight: 400; font-size: 21px;
    color: var(--ink); letter-spacing: 0.2px;
  }
  .brand__square { width: 9px; height: 9px; background: var(--green); }

  .copy p {
    font-family: "Arimo", Arial, sans-serif; font-size: 8.7px; line-height: 10.5px;
    color: var(--body); white-space: nowrap;
  }

  /* Letter */
  .letter__salutation {
    position: absolute; top: 222px; left: 46px;
    font-family: "Arimo", Arial, sans-serif; font-size: 11.5px; color: var(--body);
  }
  .letter__body { position: absolute; top: 258px; left: 46px; width: 421px; }
  .letter__body p + p { margin-top: 9.5px; }
  .letter__closing {
    position: absolute; top: 472px; left: 46px;
    font-family: "Arimo", Arial, sans-serif; font-size: 6.6px; color: var(--body);
  }
  .letter__signature {
    position: absolute; top: 496px; left: 46px; width: 64px; height: 20px;
    background: var(--sig); border-radius: 2px;
  }

  /* Report */
  .report__banner {
    position: absolute; top: 109px; left: 46px; width: 415px; height: 41px;
    background: var(--green); color: #fff;
    font-family: "Roboto Condensed", sans-serif; font-weight: 400; font-size: 36px;
    line-height: 41px; text-align: center; letter-spacing: 0.5px;
  }
  .report__section { position: absolute; left: 46px; width: 417px; }
  .report__heading {
    font-family: "Roboto Condensed", sans-serif; font-weight: 600; font-size: 17px;
    line-height: 17px; color: var(--green);
    border-bottom: 1px solid var(--rule); padding-bottom: 1px; width: 415px;
  }
  .report__section .copy { margin-top: 7px; }
  .report__section .copy p + p { margin-top: 8.5px; }

  /* Footer */
  .footer {
    position: absolute; top: 693px; left: 0; width: 100%; text-align: center;
    font-family: "Roboto", sans-serif; font-size: 8.4px; color: var(--body);
  }
  .footer__name { color: var(--green); font-weight: 700; }
  .footer__sep { color: var(--green); font-weight: 700; margin: 0 1px; }
  .footer__icon { display: inline-block; width: 7px; height: 7px; vertical-align: -0.5px; margin-right: 1px; }
  .footer-bar { position: absolute; bottom: 0; left: 0; width: 100%; height: 6px; display: flex; gap: 2px; }
  .footer-bar__green { flex: 1; background: var(--green); }
  .footer-bar__black { flex: 1; background: var(--ink); }
</style>
</head>
<body>
<div class="canvas">

  <!-- Letterhead -->
  <section class="page page--letter">
    <div class="brand"><span class="brand__square"></span><span>Kinward Advisory</span></div>

    <p class="letter__salutation">Dear Mr. Lawson,</p>
    <div class="letter__body copy">
      <p>Lorem ipsum dolor sit amet, consectetuer adipiscing elit, sed diam nonmmy nibh euismod tincidunt ut laor<br>eet dolore magna aliquam erat volutpat. Ut wisi enim ad minim veniam, quis nostrud exerci tationmcorper<br>suscipit lobortis nisl ut aliquip ex ea commodo consequat. Duis autem vel eum iriure dolor in hendrerit in<br>vulputate velit esse molestie consequat, vel illum dolore eu feugiat</p>
      <p>Rorem ipsum dolor sit amet, consectetuer adipiscing elit, sed diam nonmmy nibh euismod tincidunt ut laor<br>eet dolore magna aliquam erat volutpat. Ut wisi enim ad minim veniam, quis nostrud exerci tationmcorper<br>suscipit lobortis nisl ut aliquip ex ea commodo consequat. Duis autem vel eum iriure dolor in hendrerit in<br>vulputate velit esse molest</p>
      <p>Dorem ipsum dolor sit amet, consectetuer adipiscing elit, sed diam nonmmy nibh euismod tincidunt ut laor<br>eet dolore magna aliquam erat volutpat. Ut wisi enim ad minim veniam, quis nostrud exerci tationmcorper<br>suscipit lobortis nisl ut aliquip ex ea commodo consequat. Duis autem vel eum iriure dolor in hendrerit in<br>suscipit lobortis nisl ut aliquip ex ea commodo consequat. Duis autem vel eum iriure dolor in hendrerit in<br>vulputate velit esse molestie consequat, vel illum</p>
      <p>Sorem ipsum dolor sit amet, consectetuer adipiscing elit, sed diam nonmmy nibh euismod tincidunt ut laor<br>eet dolore magna aliquam erat volutpat. Ut wisi enim ad minim veniam, quis nostrud exerci tationmcorper<br>suscipit lobortis nisl ut aliquip ex ea commodo consequat. Duis autem vel eum iriure dolor in</p>
    </div>
    <p class="letter__closing">Sincerely,</p>
    <div class="letter__signature" role="img" aria-label="Handwritten signature"></div>

    <p class="footer">
      <span class="footer__name">Jonah Pettifer</span><span class="footer__sep"> | </span>Managing Director<span class="footer__sep"> | </span>
      <svg class="footer__icon" viewBox="0 0 10 10" aria-hidden="true"><path fill="#2a9a47" d="M2.2 0.6 3.9 2.8 3 4c.6 1.2 1.6 2.2 3 3l1.2-.9 2.2 1.7-1 1.6C5 9.6.4 5 .6 1.6Z"/></svg>0400 555 019
    </p>
    <div class="footer-bar"><span class="footer-bar__green"></span><span class="footer-bar__black"></span></div>
  </section>

  <!-- Report -->
  <section class="page page--report">
    <div class="brand"><span class="brand__square"></span><span>Kinward Advisory</span></div>

    <h1 class="report__banner">ANNUAL REPORT 2025</h1>

    <div class="report__section" style="top:167px">
      <h2 class="report__heading">Title:</h2>
      <div class="copy">
        <p>Lorem ipsum dolor sit amet, consectetuer adipiscing elit, sed diam nonmmy nibh euismod tincidunt ut laor<br>eet dolore magna aliquam erat volutpat. Ut wisi enim ad minim veniam, quis nostrud exerci tationmcorper<br>suscipit lobortis nisl ut aliquip ex ea commodo consequat. Duis autem vel eum iriure dolor in hendrerit in<br>vulputate velit esse molestie consequat, vel illum dolore eu feugiat</p>
      </div>
    </div>

    <div class="report__section" style="top:249px">
      <h2 class="report__heading">Table of contents:</h2>
      <div class="copy">
        <p>Lorem ipsum dolor sit amet, consectetuer adipiscing elit, sed diam nonmmy nibh euismod tincidunt ut laor<br>eet dolore magna aliquam erat volutpat. Ut wisi enim ad minim veniam, quis nostrud exerci tationmcorper<br>suscipit lobortis nisl ut aliquip ex ea commodo consequat. Duis autem vel eum iriure dolor in hendrerit in<br>vulputate velit esse molestie consequat, vel illum dolore eu feugiat</p>
        <p>Rorem ipsum dolor sit amet, consectetuer adipiscing elit, sed diam nonmmy nibh euismod tincidunt ut laor<br>eet dolore magna aliquam erat volutpat. Ut wisi enim ad minim veniam, quis nostrud exerci tationmcorper<br>suscipit lobortis nisl ut aliquip ex ea commodo consequat. Duis autem vel eum iriure dolor in hendrerit in<br>vulputate velit esse molest</p>
      </div>
    </div>

    <div class="report__section" style="top:381px">
      <h2 class="report__heading">Executive Summary:</h2>
      <div class="copy">
        <p>Lorem ipsum dolor sit amet, consectetuer adipiscing elit, sed diam nonmmy nibh euismod tincidunt ut laor<br>eet dolore magna aliquam erat volutpat. Ut wisi enim ad minim veniam, quis nostrud exerci tationmcorper<br>suscipit lobortis nisl ut aliquip ex ea commodo consequat. Duis autem vel eum iriure dolor in hendrerit in<br>vulputate velit esse molestie consequat, vel illum dolore eu feugiat</p>
      </div>
    </div>

    <div class="report__section" style="top:465px">
      <h2 class="report__heading">Quick Summary (Introduction):</h2>
      <div class="copy">
        <p>Lorem ipsum dolor sit amet, consectetuer adipiscing elit, sed diam nonmmy nibh euismod tincidunt ut laor<br>eet dolore magna aliquam erat volutpat. Ut wisi enim ad minim veniam, quis nostrud exerci tationmcorper<br>suscipit lobortis nisl ut aliquip ex ea commodo consequat. Duis autem vel eum iriure dolor in hendrerit in<br>vulputate velit esse molestie consequat, vel illum dolore eu feugiat</p>
        <p>Rorem ipsum dolor sit amet, consectetuer adipiscing elit, sed diam nonmmy nibh euismod tincidunt ut laor<br>eet dolore magna aliquam erat volutpat. Ut wisi enim ad minim veniam, quis nostrud exerci tationmcorper<br>suscipit lobortis nisl ut aliquip ex ea commodo consequat. Duis autem vel eum iriure dolor in hendrerit in<br>vulputate velit esse molest</p>
      </div>
    </div>

    <div class="report__section" style="top:592px">
      <h2 class="report__heading">Conclusion:</h2>
      <div class="copy">
        <p>Lorem ipsum dolor sit amet, consectetuer adipiscing elit, sed diam nonmmy nibh euismod tincidunt ut laor<br>eet dolore magna aliquam erat volutpat. Ut wisi enim ad minim veniam, quis nostrud exerci tationmcorper<br>suscipit lobortis nisl ut aliquip ex ea commodo consequat. Duis autem vel eum iriure dolor in hendrerit in<br>vulputate velit esse molestie consequat, vel illum dolore eu feugiat</p>
      </div>
    </div>

    <p class="footer">
      <span class="footer__name">Jonah Pettifer</span><span class="footer__sep"> | </span>Managing Director<span class="footer__sep"> | </span>
      <svg class="footer__icon" viewBox="0 0 10 10" aria-hidden="true"><path fill="#2a9a47" d="M2.2 0.6 3.9 2.8 3 4c.6 1.2 1.6 2.2 3 3l1.2-.9 2.2 1.7-1 1.6C5 9.6.4 5 .6 1.6Z"/></svg>0400 555 019
    </p>
    <div class="footer-bar"><span class="footer-bar__green"></span><span class="footer-bar__black"></span></div>
  </section>

</div>
</body>
</html>
```